Brisk Haven Web Site design

I need to build an exciting, colorful web site to market our business. I already used your services to design our logo with Dorian. Design # 40957286.
Our company sells a trademarked system for cleaning up water damage in buildings across the United States. This work is billed directly through insurance companies and has a high profit margin.

Target Market(s)

Men. 25-55 yrs old who want to own there own business

Industry/Entity Type

Cleaning Service

Number of Pages Required

4 page

Font styles to use
Sans Serif

Requirements
Must have
• Our trademarked logo as designed by Dorian
• Our phone number: 866-4BRISKH (866-427-4754)
• Pictures of flooded homes and businesses.
• List of our services: Water removal, carpet and tile cleaning, mold remediation, and trauma clean up services.
• Photos of our truck as designed by Dorian
• Photos of an attractive operator standing buy to take a call.
• Photos of happy homeowners
Nice to have
• Call to action text
• "Proven system"text
• "Be your own boss" text

```html
<!DOCTYPE html>
<html lang="en">
<head>
<meta charset="utf-8">
<title>Brisk Haven — Water Removal and Carpet Cleaning</title>
<link href="https://fonts.googleapis.com/css2?family=Poppins:wght@400;600;700&family=Open+Sans:wght@400;600;700&display=swap" rel="stylesheet">
<style>
:root{
  --blue:#1b3fc4;
  --blue-dark:#10288f;
  --blue-light:#2d8cf0;
  --sky:#3aa4f2;
  --ink:#111418;
  --text:#444b55;
  --white:#ffffff;
  --footer:#121417;
  --footer-line:#2a2d33;
}
*{margin:0;padding:0;box-sizing:border-box}
html,body{width:1200px;height:2276px;overflow:hidden;background:var(--white)}
body{font-family:"Open Sans",Arial,sans-serif;color:var(--text);position:relative}
.heading{font-family:"Poppins",Arial,sans-serif}

/* header */
.site-header{position:absolute;top:0;left:0;width:1200px;height:124px;background:var(--white)}
.header-van{position:absolute;left:14px;top:8px;width:122px;height:62px;border-radius:10px;background:linear-gradient(135deg,#dfe6f3,#9fb3d6)}
.brand{position:absolute;left:350px;top:24px;text-align:center;width:260px}
.brand-name{display:flex;align-items:center;justify-content:center;gap:10px;font-family:"Poppins",Arial,sans-serif;font-weight:700;font-size:34px;color:var(--blue);line-height:1}
.brand-dot{width:26px;height:26px;border-radius:50%;background:var(--blue)}
.brand-phone{font-family:"Poppins",Arial,sans-serif;font-weight:700;font-size:15px;color:var(--blue);margin-top:10px;letter-spacing:1px}
.mail-line{position:absolute;left:710px;top:12px;display:flex;align-items:center;gap:10px}
.mail-icon{width:26px;height:26px;border-radius:50%;background:var(--blue-light);display:flex;align-items:center;justify-content:center}
.mail-text{font-size:11px;line-height:1.3;color:var(--ink)}
.mail-text strong{display:block;font-weight:700}
.call-btn{position:absolute;right:14px;top:10px;height:34px;padding:0 14px;background:var(--sky);border-radius:4px;display:flex;align-items:center;gap:8px;color:var(--white);font-weight:700;font-size:18px}
.social{position:absolute;right:14px;top:70px;display:flex;gap:6px}
.social span{width:26px;height:26px;border-radius:50%;background:#2a2d33;display:block}

.main-nav{position:absolute;top:124px;left:0;width:1200px;height:40px;background:var(--blue);display:flex;align-items:center;padding-left:56px}
.main-nav a{color:var(--white);text-decoration:none;font-family:"Poppins",Arial,sans-serif;font-weight:600;font-size:13px;padding:0 20px;height:40px;line-height:40px}
.main-nav a.active{background:var(--blue-dark)}

/* hero */
.hero{position:absolute;top:164px;left:0;width:1200px;height:460px;background:linear-gradient(100deg,#2b6f7a 0%,#6fb0b3 35%,#d8dcd8 70%,#bfc6c4 100%)}
.hero-caption{position:absolute;left:62px;top:172px;width:390px}
.hero-caption .label{background:rgba(58,164,242,.85);padding:6px 12px 4px;display:inline-block}
.hero-title{font-family:"Poppins",Arial,sans-serif;font-weight:700;font-size:38px;color:var(--white);line-height:1}
.hero-sub{font-family:"Poppins",Arial,sans-serif;font-weight:600;font-size:20px;color:#0d2a7a;background:rgba(58,164,242,.85);padding:4px 12px;margin-top:0}
.hero-lead{font-family:"Poppins",Arial,sans-serif;font-weight:700;font-size:30px;color:var(--white);background:rgba(58,164,242,.85);padding:2px 12px 8px}
.btn-dark{display:inline-block;margin-top:12px;background:var(--blue-dark);color:var(--white);font-size:15px;padding:10px 24px;border-radius:3px}

/* intro */
.intro{position:absolute;top:624px;left:0;width:1200px;height:356px;background:var(--white)}
.intro h1{position:absolute;left:62px;top:62px;font-size:38px;font-weight:700;color:var(--ink)}
.intro .tagline{position:absolute;left:62px;top:112px;font-size:18px;font-weight:600;color:var(--blue);font-family:"Poppins",Arial,sans-serif}
.intro .copy{position:absolute;left:62px;top:172px;width:600px;font-size:14px;line-height:1.6}
.intro .copy p+p{margin-top:14px}
.intro-truck{position:absolute;left:800px;top:90px;width:350px;height:160px;border-radius:14px;background:linear-gradient(135deg,#eef2f8,#b9c7e0)}

/* services */
.services{position:absolute;top:980px;left:0;width:1200px;height:790px;background:linear-gradient(180deg,#1b44d8,#1433b8)}
.services h2{text-align:center;color:var(--white);font-size:50px;font-weight:600;margin-top:110px}
.services .sub{text-align:center;color:#dbe4ff;font-size:14px;margin-top:4px}
.service-grid{position:absolute;top:260px;left:70px;width:1060px;display:flex;justify-content:space-between}
.service{width:220px;text-align:center}
.service-icon{width:120px;height:120px;margin:0 auto;border-radius:14px;background:rgba(255,255,255,.85)}
.service h3{color:var(--white);font-size:18px;font-weight:600;margin-top:40px;font-family:"Poppins",Arial,sans-serif}
.service p{color:#e2e8ff;font-size:12px;line-height:1.55;margin-top:10px}
.btn-light{display:inline-block;margin-top:86px;background:var(--sky);color:var(--white);font-size:14px;padding:8px 22px;border-radius:3px}

/* call to action */
.cta{position:absolute;top:1770px;left:0;width:1200px;height:180px;text-align:center;background:var(--white)}
.cta h2{margin-top:48px;color:var(--blue);font-size:36px;font-weight:600}
.cta .call{margin-top:16px;display:flex;justify-content:center;align-items:center;gap:14px;font-size:17px;color:var(--ink)}
.cta .call span.num{background:var(--sky);color:var(--white);font-weight:700;padding:6px 14px;border-radius:3px}

/* footer */
.site-footer{position:absolute;top:1950px;left:0;width:1200px;height:302px;background:var(--footer);color:#cfd3da}
.site-footer h4{color:var(--white);font-family:"Poppins",Arial,sans-serif;font-weight:600;font-size:18px}
.f-contact{position:absolute;left:62px;top:28px;width:300px}
.f-row{display:flex;gap:10px;font-size:12px;line-height:1.5;margin-top:18px}
.f-row i{width:14px;height:14px;flex:none;margin-top:2px;display:block}
.f-links{position:absolute;left:400px;top:28px;width:330px}
.f-links .cols{display:flex;gap:70px;margin-top:18px}
.f-links ul{list-style:none;font-size:12px;line-height:2.1}
.f-links li::before{content:"› ";color:var(--sky)}
.f-query{position:absolute;left:760px;top:28px;width:380px}
.f-query .row{display:flex;gap:10px;margin-top:16px}
.f-query .field{background:#e9ebee;height:30px;flex:1}
.f-query .area{background:#e9ebee;height:80px;margin-top:10px}
.f-query .send{float:right;margin-top:10px;background:var(--sky);color:var(--white);font-size:13px;padding:6px 16px}
.copyright{position:absolute;top:2252px;left:0;width:1200px;height:24px;background:#0b0c0e;color:#8b9099;font-size:11px;text-align:center;line-height:24px}
</style>
</head>
<body>

<header class="site-header">
  <div class="header-van" role="img" aria-label="Brisk Haven service van"></div>
  <div class="brand">
    <div class="brand-name"><span class="brand-dot"></span>Brisk Haven</div>
    <div class="brand-phone">866-427-4754</div>
  </div>
  <div class="mail-line">
    <div class="mail-icon"><svg width="14" height="10" viewBox="0 0 14 10"><rect x="0.5" y="0.5" width="13" height="9" fill="none" stroke="#fff"/><path d="M0.5 0.5 L7 5.5 L13.5 0.5" fill="none" stroke="#fff"/></svg></div>
    <div class="mail-text"><strong>Mail us and solve your problem!</strong>mara.quinlan@example.com</div>
  </div>
  <div class="call-btn"><svg width="16" height="16" viewBox="0 0 24 24"><path fill="#fff" d="M6.6 10.8a15.1 15.1 0 0 0 6.6 6.6l2.2-2.2a1 1 0 0 1 1-.25 11.4 11.4 0 0 0 3.6.57 1 1 0 0 1 1 1V20a1 1 0 0 1-1 1A17 17 0 0 1 3 4a1 1 0 0 1 1-1h3.5a1 1 0 0 1 1 1c0 1.25.2 2.45.57 3.57a1 1 0 0 1-.25 1z"/></svg>03 555 0192</div>
  <div class="social"><span></span><span></span><span></span></div>
</header>

<nav class="main-nav">
  <a class="active" href="#">HOME</a>
  <a href="#">FIRE &amp; WATER MOLD</a>
  <a href="#">CLEANING INSURANCE</a>
  <a href="#">COMMERCIAL</a>
  <a href="#">FRANCHISING</a>
  <a href="#">CORPORATE</a>
  <a href="#">CONTACT US</a>
</nav>

<section class="hero" role="img" aria-label="Technician cleaning a carpet with an extraction wand in a bright room">
  <div class="hero-caption">
    <div class="label"><div class="hero-title">CLEANING</div></div>
    <div class="hero-sub">WATER CLEANING SERVICES</div>
    <div class="hero-lead">Professional carpet cleaning</div>
    <span class="btn-dark">Contact us</span>
  </div>
</section>

<section class="intro">
  <h1 class="heading">Water removal and carpet cleaning</h1>
  <div class="tagline">We are dealing with water damage, immediate action is crucial.</div>
  <div class="copy">
    <p>When you are dealing with water damage, immediate action is crucial. RestorePro Franchise Professionals respond immediately and use advanced equipment and techniques to remove the water quickly. They closely monitor and document the drying process to verify your property is dried properly and thoroughly.</p>
    <p>Please refer to our Water Damage Tips - Until Help Arrives Guide and follow these tips to protect yourself and your property.</p>
  </div>
  <div class="intro-truck" role="img" aria-label="Brisk Haven branded service van"></div>
</section>

<section class="services">
  <h2 class="heading">Our Services</h2>
  <div class="sub">We are dealing with water damage, immediate action is crucial.</div>
  <div class="service-grid">
    <div class="service">
      <div class="service-icon" role="img" aria-label="Water removal icon"></div>
      <h3>Water removal</h3>
      <p>Franchise Professionals specialize in water damage restoration, the cornerstone of our business.</p>
      <span class="btn-light">Read More</span>
    </div>
    <div class="service">
      <div class="service-icon" role="img" aria-label="Carpet and tile cleaning icon"></div>
      <h3>Carpet and tile cleaning</h3>
      <p>Franchise Professionals specialize in water damage restoration, the cornerstone of our business.</p>
      <span class="btn-light">Read More</span>
    </div>
    <div class="service">
      <div class="service-icon" role="img" aria-label="Mold remediation icon"></div>
      <h3>Mold Remediation</h3>
      <p>Franchise Professionals specialize in water damage restoration, the cornerstone of our business.</p>
      <span class="btn-light">Read More</span>
    </div>
    <div class="service">
      <div class="service-icon" role="img" aria-label="Trauma clean up icon"></div>
      <h3>Trauma clean up</h3>
      <p>Franchise Professionals specialize in water damage restoration, the cornerstone of our business.</p>
      <span class="btn-light">Read More</span>
    </div>
  </div>
</section>

<section class="cta">
  <h2 class="heading">Get Started With Our Service</h2>
  <div class="call">
    <svg width="18" height="18" viewBox="0 0 24 24"><path fill="#1b3fc4" d="M6.6 10.8a15.1 15.1 0 0 0 6.6 6.6l2.2-2.2a1 1 0 0 1 1-.25 11.4 11.4 0 0 0 3.6.57 1 1 0 0 1 1 1V20a1 1 0 0 1-1 1A17 17 0 0 1 3 4a1 1 0 0 1 1-1h3.5a1 1 0 0 1 1 1c0 1.25.2 2.45.57 3.57a1 1 0 0 1-.25 1z"/></svg>
    Call us today at <span class="num">866-427-4754</span>
  </div>
</section>

<footer class="site-footer">
  <div class="f-contact">
    <h4>Contact Info</h4>
    <div class="f-row"><i><svg width="14" height="14" viewBox="0 0 24 24"><path fill="#3aa4f2" d="M12 2a7 7 0 0 0-7 7c0 5 7 13 7 13s7-8 7-13a7 7 0 0 0-7-7zm0 9.5A2.5 2.5 0 1 1 12 6.5a2.5 2.5 0 0 1 0 5z"/></svg></i><span>Harbor Point Marina - 14 Lantern Way, Bayview Dock</span></div>
    <div class="f-row"><i><svg width="14" height="14" viewBox="0 0 24 24"><path fill="#3aa4f2" d="M6.6 10.8a15.1 15.1 0 0 0 6.6 6.6l2.2-2.2a1 1 0 0 1 1-.25 11.4 11.4 0 0 0 3.6.57 1 1 0 0 1 1 1V20a1 1 0 0 1-1 1A17 17 0 0 1 3 4a1 1 0 0 1 1-1h3.5a1 1 0 0 1 1 1c0 1.25.2 2.45.57 3.57a1 1 0 0 1-.25 1z"/></svg></i><span>813-555-0147</span></div>
    <div class="f-row"><i><svg width="14" height="14" viewBox="0 0 14 10"><rect x="0.5" y="0.5" width="13" height="9" fill="none" stroke="#3aa4f2"/><path d="M0.5 0.5 L7 5.5 L13.5 0.5" fill="none" stroke="#3aa4f2"/></svg></i><span>mara.quinlan@example.com</span></div>
  </div>
  <div class="f-links">
    <h4>Quick Links</h4>
    <div class="cols">
      <ul><li>Home</li><li>About Us</li><li>Contact Us</li><li>Sitemap</li><li>Customer Login</li></ul>
      <ul><li>Home</li><li>About Us</li><li>Contact Us</li><li>Sitemap</li><li>Customer Login</li></ul>
    </div>
  </div>
  <div class="f-query">
    <h4>Query us</h4>
    <div class="row"><div class="field"></div><div class="field"></div></div>
    <div class="area"></div>
    <span class="send">Send</span>
  </div>
</footer>
<div class="copyright">Copyright © 2016 Brisk Haven, All rights reserved</div>

</body>
</html>
```